Brochure Design Project

I require a brochure with inserts inside that show our different services for different industries.

The insides of the brochure will have "about our company" ie, trackered vans - pda's and software used - images of the team and showing we invest in the very latest equipment and softwares to offer the best highest quality service. etc etc then the inserts demonstrating what we can do for each industry - images working on sites, equipment used etc etc on the back of each sheet a case study proving implementation.

Construction
Public Transport
Hotel & Leisure
Retail / Businesses
Housing Association

The inserts I imagine will be different in size or cut differently down the sides in order to allow the reader to see the different sectors and go to the one they require. The brochure will go in full to some companies - like facilities management whom would be interested in all the work we do for industries - however the brochure may contain just one of the inserts if we visit say a construction site in which they would only be interested in one (construction)

The inserts will show all the services we offer for that industry and maybe to the rear have a case study in which proves our implementation of service.

Our overall company is to offer solutions for damaged , worn or complete change of style to surfaces. For example we offer invisible damage repairs to surfaces like woods, laminates, ceramics etc.
We offer full scale resurfacing from bath re-enamelling to commercial spraying of powdercoating, metal work on offices.

also must have slot for business card.

Our communication to the customer is that using our services you can repair or resurface items back to new at the fraction of the cost of replacement thus reducing landfil as you are replacing not repairing. You get the brand new finish for a lot less cost - time and mess.

VELTAR - cutting cost with the environment in mind.

Target Market(s)

Various sectors as indicated. Business card slot.

Industry/Entity Type

Communication

Requirements
Must have
• inserts cut down the side in a way that looks good when one single insert is added but all look great showing through each sector when all added together.

```html
<!DOCTYPE html>
<html lang="en">
<head>
<meta charset="utf-8">
<title>VELTAR Company Brochure</title>
<link rel="stylesheet" href="https://fonts.googleapis.com/css2?family=Open+Sans:ital,wght@0,400;0,600;1,400&display=swap">
<style>
  :root {
    --cover-black: #000000;
    --page-bg: #ffffff;
    --brand-green: #8dc63f;
    --text-light: #f2f2f2;
    --name-grey: #e4e4e4;
    --tab-border: #9a9a9a;
    --tab-text-dark: #111111;
    --cut-mark: #d6246e;
  }
  * { margin: 0; padding: 0; box-sizing: border-box; }
  html, body {
    width: 848px; height: 1200px; overflow: hidden;
    background: var(--page-bg);
    font-family: "Open Sans", Arial, sans-serif;
  }
  .brochure { position: relative; width: 848px; height: 1200px; }
  .cover {
    position: absolute; left: 0; top: 0; width: 798px; height: 1200px;
    background: var(--cover-black);
  }
  .cover-top-tab {
    position: absolute; left: 780px; top: 0; width: 68px; height: 170px;
    background: var(--cover-black); border-top-right-radius: 28px;
    border-bottom-right-radius: 28px;
  }
  .sector-tab {
    position: absolute; left: 798px; width: 50px;
    border-top-right-radius: 26px; border-bottom-right-radius: 26px;
    display: flex; align-items: flex-start; justify-content: center;
    padding-top: 34px;
  }
  .sector-tab span {
    writing-mode: vertical-rl; font-size: 13px; white-space: nowrap;
  }
  .tab-green { background: var(--brand-green); color: var(--tab-text-dark); }
  .tab-white { background: var(--page-bg); color: var(--tab-text-dark); border: 1px solid var(--tab-border); border-left: none; }
  .tab-black { background: var(--cover-black); color: var(--text-light); }
  .tab-construction { top: 164px; height: 168px; z-index: 5; }
  .tab-transport { top: 326px; height: 164px; z-index: 4; }
  .tab-hotel { top: 484px; height: 168px; z-index: 3; }
  .tab-retail { top: 646px; height: 162px; z-index: 2; }
  .tab-housing { top: 802px; height: 168px; z-index: 1; }

  .brand-mark {
    position: absolute; left: 313px; top: 192px; width: 228px; height: 228px;
    border-radius: 50%; background: #2b2b2b;
  }
  .brand-name {
    position: absolute; left: 0; width: 798px; top: 420px; text-align: center;
    font-size: 146px; font-weight: 400; line-height: 1; letter-spacing: 4px;
    color: var(--name-grey);
  }
  .tagline {
    position: absolute; left: 0; width: 798px; top: 620px; text-align: center;
    font-size: 26px; letter-spacing: 2px; color: var(--brand-green);
  }
  .doc-title {
    position: absolute; left: 0; width: 798px; top: 710px; text-align: center;
    font-size: 43px; font-style: italic; color: var(--text-light); letter-spacing: 1px;
  }
  .card-slot { position: absolute; left: 290px; top: 850px; }
  .strapline {
    position: absolute; left: 298px; top: 1146px;
    font-size: 20px; color: var(--text-light); letter-spacing: 0.5px;
  }
  .strapline em { font-style: normal; color: var(--brand-green); }
</style>
</head>
<body>
<main class="brochure">
  <div class="cover-top-tab"></div>
  <div class="cover"></div>

  <div class="sector-tab tab-green tab-construction"><span>Construction</span></div>
  <div class="sector-tab tab-white tab-transport"><span>Public Transport</span></div>
  <div class="sector-tab tab-black tab-hotel"><span>Hotel &amp; Leisure</span></div>
  <div class="sector-tab tab-green tab-retail"><span>Retail/Businesses</span></div>
  <div class="sector-tab tab-white tab-housing"><span>Housing Association</span></div>

  <div class="brand-mark" aria-hidden="true"></div>
  <h1 class="brand-name">VELTAR</h1>
  <p class="tagline">REPAIR · RESTORE · RESURFACE</p>
  <h2 class="doc-title">Company Brochure</h2>

  <svg class="card-slot" width="420" height="300" viewBox="0 0 420 300" aria-label="Business card slot">
    <rect x="23" y="23" width="362" height="243" fill="none" stroke="#ffffff" stroke-width="1.5"/>
    <line x1="355" y1="0" x2="400" y2="45" stroke="var(--cut-mark)" stroke-width="1.5"/>
    <line x1="0" y1="245" x2="45" y2="290" stroke="var(--cut-mark)" stroke-width="1.5"/>
  </svg>

  <p class="strapline">Cutting cost with <em>the environment</em> in mind</p>
</main>
</body>
</html>
```